Corvane Industries business cards

We need business cards for our company Corvane Industries, based in Brisbane but trading world wide. We buy and sell Corvane Industries, generators and marine equipment. The design needs to be kept clean, simple but eye catching.
Please keep with our current logo (included) and further information can be included on request

Business

0792cd
33a6d7
85cae6
3276b5
0455a3
cedeed
cee9f5
ffffff

```html
<!DOCTYPE html>
<html lang="en">
<head>
<meta charset="UTF-8">
<title>Corvane Industries – Business Card</title>
<link href="https://fonts.googleapis.com/css2?family=Roboto:wght@500&family=Quicksand:wght@500;600&display=swap" rel="stylesheet">
<style>
  :root {
    --page-bg: #e9edf1;
    --card-white: #ffffff;
    --brand-blue: #4a87c5;
    --swoosh-grey: #8b8f94;
    --text-white: #ffffff;
  }
  * { margin: 0; padding: 0; box-sizing: border-box; }
  html, body {
    width: 1200px; height: 900px; overflow: hidden;
    background: var(--page-bg);
  }
  .canvas { position: relative; width: 1200px; height: 900px; }
  .card {
    position: absolute; left: 100px; top: 150px;
    width: 1000px; height: 600px;
    background: var(--card-white);
    border-radius: 44px; overflow: hidden;
    box-shadow: 0 12px 36px rgba(20, 40, 70, 0.18);
  }
  .card-wave { position: absolute; inset: 0; width: 100%; height: 100%; }
  .wave-fill { fill: var(--brand-blue); }
  .wave-swoosh { fill: var(--swoosh-grey); }

  .brand {
    position: absolute; left: 70px; top: 78px;
    display: flex; align-items: flex-start; gap: 22px;
  }
  .brand-mark {
    width: 112px; height: 112px; border-radius: 14px;
    background: var(--brand-blue); margin-top: 6px;
  }
  .brand-name {
    font-family: "Roboto", sans-serif; font-weight: 500;
    color: var(--brand-blue); font-size: 56px; line-height: 1.0;
    display: flex; flex-direction: column;
  }
  .brand-suffix { font-size: 20px; align-self: flex-end; margin-top: 4px; }

  .contact {
    position: absolute; right: 56px; top: 244px;
    font-family: "Quicksand", sans-serif; font-weight: 500;
    color: var(--text-white); text-align: right;
  }
  .contact-name { font-size: 26px; letter-spacing: 1px; line-height: 1.2; }
  .contact-title { font-size: 15px; letter-spacing: 2px; margin-bottom: 16px; }
  .contact-row {
    display: flex; justify-content: flex-end; align-items: center;
    gap: 12px; font-size: 21px; height: 37px;
  }
  .contact-row svg { width: 21px; height: 21px; fill: none; stroke: var(--text-white); stroke-width: 2; }
  .contact-row svg .solid { fill: var(--text-white); stroke: none; }
  .address {
    position: absolute; right: 56px; bottom: 44px;
    font-family: "Quicksand", sans-serif; font-weight: 600;
    color: var(--text-white); font-size: 25px; letter-spacing: 0.5px;
  }
</style>
</head>
<body>
<main class="canvas">
  <section class="card" aria-label="Corvane Industries business card">
    <svg class="card-wave" viewBox="0 0 1000 600" preserveAspectRatio="none" aria-hidden="true">
      <path class="wave-swoosh" d="M0 292 C150 372 300 402 430 376 C630 330 800 150 1000 76 L1000 92 C800 168 630 350 430 396 C300 424 150 404 0 318 Z"/>
      <path class="wave-fill" d="M0 336 C150 420 300 444 430 418 C630 360 800 180 1000 110 L1000 600 L0 600 Z"/>
    </svg>

    <header class="brand">
      <div class="brand-mark" aria-hidden="true"></div>
      <div class="brand-name">
        <span>Corvane</span>
        <span>Industries</span>
        <span class="brand-suffix">Pty Ltd</span>
      </div>
    </header>

    <div class="contact">
      <p class="contact-name">ELENA VARGA</p>
      <p class="contact-title">PRESIDENT</p>
      <p class="contact-row">012 555 0148
        <svg viewBox="0 0 24 24"><path d="M5 3h4l2 5-3 2a12 12 0 0 0 6 6l2-3 5 2v4a2 2 0 0 1-2 2A18 18 0 0 1 3 5a2 2 0 0 1 2-2z"/></svg>
      </p>
      <p class="contact-row">012 555 0162
        <svg viewBox="0 0 24 24"><rect x="7" y="2" width="10" height="20" rx="2"/><circle class="solid" cx="12" cy="18.5" r="1.2"/></svg>
      </p>
      <p class="contact-row">012 555 0177
        <svg viewBox="0 0 24 24"><rect x="3" y="9" width="18" height="10" rx="1"/><rect x="7" y="3" width="10" height="6"/><line x1="7" y1="14" x2="17" y2="14"/></svg>
      </p>
      <p class="contact-row">elena@corvanemail.com
        <svg viewBox="0 0 24 24"><rect x="3" y="5" width="18" height="14" rx="1"/><path d="M3 6l9 7 9-7"/></svg>
      </p>
      <p class="contact-row">www.corvaneweb.com
        <svg viewBox="0 0 24 24"><circle cx="12" cy="12" r="9"/><ellipse cx="12" cy="12" rx="4" ry="9"/><line x1="3" y1="12" x2="21" y2="12"/></svg>
      </p>
    </div>

    <p class="address">041 9th floor Harbour Point Road Qld</p>
  </section>
</main>
</body>
</html>
```